4 Page Music Brochure design

We need assistance in designing a 4 Page A4 (A3 folded) Brochure promoting International Music Tour options for school groups. We have included text in the brief as well as images to be used in the brochure.

```html
<!DOCTYPE html>
<html lang="en">
<head>
<meta charset="utf-8">
<title>Music Tours Brochure Spread</title>
<link href="https://fonts.googleapis.com/css2?family=Archivo+Black&family=Montserrat:wght@400;600;700&display=swap" rel="stylesheet">
<style>
  :root{
    --brand-red:#b5121b;
    --deep-red:#8e0d14;
    --ink:#2e2e2e;
    --paper:#ffffff;
    --backdrop:#e7e5e2;
    --rule:#c9c9c9;
  }
  *{box-sizing:border-box;margin:0;padding:0}
  html,body{width:1200px;height:870px;overflow:hidden;background:var(--backdrop)}
  body{font-family:"Montserrat",sans-serif;color:var(--ink);position:relative}
  .spread{position:absolute;left:20px;top:25px;width:1160px;height:820px;display:flex;box-shadow:0 6px 24px rgba(0,0,0,.18)}
  .page{position:relative;width:580px;height:820px;background:var(--paper);overflow:hidden}
  .page--left{border-right:1px solid #e2e2e2}
  .heading{font-family:"Archivo Black",sans-serif;color:var(--brand-red);font-weight:400;letter-spacing:.5px}
  .heading .mark{display:inline-block;width:8px;height:8px;background:var(--brand-red);margin-left:8px;vertical-align:middle}
  .body-copy{font-size:10.5px;line-height:1.55;text-align:justify}
  .photo{position:absolute}
  .rule-accent{position:absolute;height:3px;background:var(--brand-red)}

  /* left page */
  .event-band{position:absolute;right:0;top:0}
  .event-title{position:absolute;right:30px;top:22px;text-align:right;color:#fff}
  .event-title h2{font-family:"Archivo Black",sans-serif;font-size:22px;font-weight:400;padding-bottom:6px;border-bottom:1px solid rgba(255,255,255,.8)}
  .event-title p{font-family:"Archivo Black",sans-serif;font-size:14px;margin-top:6px}
  .event-title sup{font-size:9px}
  .event-heading{position:absolute;left:40px;top:140px;width:430px;font-size:19px;line-height:1.25}
  .event-copy{position:absolute;left:40px;top:205px;width:420px;font-weight:600}
  .brand-vertical{position:absolute;right:-38px;top:200px;transform:rotate(90deg);transform-origin:center;font-family:"Archivo Black",sans-serif;color:var(--brand-red);text-align:center;line-height:1}
  .brand-vertical .brand-name{font-size:22px;letter-spacing:1px}
  .brand-vertical .brand-sub{font-size:11px;letter-spacing:2.5px;margin-top:2px}
  .cathedral-frame{position:absolute;left:282px;top:290px;width:260px;height:240px;border:1px solid var(--brand-red)}
  .cathedral{left:300px;top:305px;width:225px;height:195px;background:linear-gradient(180deg,#9fb3d1 0%,#c4cfde 45%,#7d7a76 70%,#55524e 100%);border:4px solid #fff;box-shadow:0 1px 4px rgba(0,0,0,.25)}
  .venue-heading{position:absolute;left:40px;top:340px;font-size:15px}
  .venue-copy{position:absolute;left:40px;top:368px;width:235px}
  .hall-block{position:absolute;left:380px;top:545px;width:175px;height:220px;background:var(--brand-red)}
  .hall{left:40px;top:520px;width:390px;height:220px;background:radial-gradient(ellipse at 50% 40%,#b07a3a 0%,#6b4018 45%,#2a1608 100%)}
  .hall-inner{position:absolute;left:60px;top:538px;width:350px;height:184px;border:1px solid rgba(255,255,255,.55)}

  /* right page */
  .japan{left:0;top:0;width:580px;height:280px;background:linear-gradient(90deg,#a8250f 0%,#d9471a 40%,#c23a14 70%,#7e1a0a 100%)}
  .brand-cutout{position:absolute;right:0;top:0}
  .brand-top{position:absolute;right:22px;top:22px;font-family:"Archivo Black",sans-serif;color:var(--brand-red);text-align:right;line-height:1}
  .brand-top .brand-name{font-size:20px;letter-spacing:1px}
  .brand-top .brand-sub{font-size:10px;letter-spacing:2.4px;margin-top:2px}
  .japan-card{position:absolute;left:30px;top:30px;width:280px;height:205px;background:rgba(255,250,245,.95);box-shadow:0 2px 8px rgba(0,0,0,.25)}
  .japan-card .card-head{background:var(--brand-red);color:#fff;padding:10px 16px;font-size:13px}
  .japan-card .card-head .mark{background:#fff}
  .japan-card .body-copy{padding:12px 16px;font-size:10px}
  .euro-heading{position:absolute;left:30px;top:305px;font-size:14px}
  .euro-copy{position:absolute;left:30px;top:330px;width:300px;font-weight:600}
  .opera-frame{position:absolute;left:345px;top:285px;width:220px;height:160px;border:1px solid var(--rule);background:#fff}
  .opera{left:355px;top:295px;width:200px;height:140px;background:radial-gradient(ellipse at 50% 30%,#d7a55a 0%,#8d4d1d 50%,#3b1e0c 100%)}
  .band-block{position:absolute;left:225px;top:470px;width:170px;height:240px;background:var(--brand-red)}
  .band{left:20px;top:492px;width:345px;height:190px;background:linear-gradient(180deg,#6f6f73 0%,#8c8888 35%,#b3262a 60%,#2b2b2b 100%)}
  .band-inner{position:absolute;left:40px;top:508px;width:305px;height:158px;border:1px solid rgba(255,255,255,.55)}
  .us-heading{position:absolute;left:405px;top:500px;width:160px;font-size:14px;line-height:1.25}
  .us-copy{position:absolute;left:405px;top:545px;width:155px;font-weight:600;font-size:10px}
</style>
</head>
<body>
<main class="spread">

  <section class="page page--left">
    <svg class="event-band" width="380" height="120" viewBox="0 0 380 120" aria-hidden="true">
      <path d="M0 0 H380 V120 H120 C60 120 20 80 0 0 Z" fill="var(--brand-red)"/>
    </svg>
    <div class="event-title">
      <h2>Global Choir Festival</h2>
      <p>(5<sup>th</sup> To The 15<sup>th</sup> Of July 2020)</p>
    </div>

    <h3 class="heading event-heading">Join The Biggest Choral Music Event In The World</h3>
    <p class="body-copy event-copy">Choirs from around the globe gather for ten days of competitions, open singing, friendship concerts and workshops. Your group can perform for audiences from many countries and regions while taking part in festival celebrations in Antwerp and Gent, Belgium, with add-on trips to nearby European countries.</p>

    <div class="brand-vertical">
      <div class="brand-name">MERIDIAN</div>
      <div class="brand-sub">GROUP TRAVEL</div>
    </div>

    <div class="cathedral-frame"></div>
    <div class="photo cathedral" role="img" aria-label="Gothic cathedral towers above a city square under a cloudy sky"></div>

    <h3 class="heading venue-heading">Grand Concert Hall<span class="mark"></span></h3>
    <p class="body-copy venue-copy">The once in a life time opportunity to perform on one of the world's most famous stages. Choirs, bands and orchestras will enjoy a concert in a premier venue in the heart of New York City, then continue on to Washington DC, Los Angeles or San Francisco to round out your trip.</p>

    <div class="hall-block"></div>
    <div class="photo hall" role="img" aria-label="Interior of a grand concert hall with warm golden balconies"></div>
    <div class="hall-inner"></div>

    <div class="rule-accent" style="left:150px;top:792px;width:120px"></div>
  </section>

  <section class="page page--right">
    <div class="photo japan" role="img" aria-label="Rows of red torii gates along a shrine path in Japan"></div>
    <svg class="brand-cutout" width="260" height="80" viewBox="0 0 260 80" aria-hidden="true">
      <path d="M0 0 C30 0 30 70 80 70 H260 V0 Z" fill="var(--paper)"/>
    </svg>
    <div class="brand-top">
      <div class="brand-name">MERIDIAN</div>
      <div class="brand-sub">GROUP TRAVEL</div>
    </div>

    <article class="japan-card">
      <h3 class="heading card-head" style="color:#fff">Japan Music Tours<span class="mark"></span></h3>
      <p class="body-copy">Travel to the land of the Rising Sun and take part in school exchanges, public performances and the chance to perform at iconic theme parks Tokyo Dreamland and Cinema Studios Japan. Students will have the opportunity to take a Japanese cooking class, partake in a traditional tea ceremony, see a Kabuki show and ride the bullet train.</p>
    </article>

    <h3 class="heading euro-heading">European Instrumental Tours<span class="mark"></span></h3>
    <p class="body-copy euro-copy">Play in Austria, France, Germany, the United Kingdom, or wherever your heart desires, your band, orchestra or ensemble will have the opportunity to perform at concert halls across Europe. As well as opportunities to participate in festivals, public performances and workshops with music professionals.</p>

    <div class="opera-frame"></div>
    <div class="photo opera" role="img" aria-label="Opera house auditorium with tiers of gilded boxes"></div>

    <div class="band-block"></div>
    <div class="photo band" role="img" aria-label="Marching band in red and white uniforms parading down a city street"></div>
    <div class="band-inner"></div>

    <h3 class="heading us-heading">US Music Road Trip<span class="mark"></span></h3>
    <p class="body-copy us-copy">Trace a path across the US journeying from Jazz to Blues to Soul onto Rock'n'Roll before finishing in Country Music capital of the world - Nashville. You will visit New Orleans, Memphis and Nashville where you will have the opportunity to perform at unique venues, undertake school exchanges and participate in workshops with musicians and professionals.</p>

    <div class="rule-accent" style="left:260px;top:792px;width:130px"></div>
  </section>

</main>
</body>
</html>
```